Mortgage Broking boutique Business

I’m wanting a revamped look to my existing business card design. I do like the black and silver but happy to have other colours introduced based on your creation. I’ve attached a copy of my current card so you can have a starting point updated details noted brloe. I deal with high net worth individuals so need my card to be sophisticated, classy that gives off a classy vibe

Target Market(s)

High net worth, wealthy

Industry/Entity Type

Mortgage Brokerage

Contact Information for Business Card

Job title: Finance Executive
Phone: +61 7 3287 4419
Mobile: 0471 352 608
Email: marcus@quillbrookcapital.com.au
Web: www.quillbrookcapital.com.au
Address: level 36 Tindale Court, 58 Harwick St Brisbane QLD 4000

Font styles to use
Other font styles liked:
• Helvetica

Colors

Designer to choose colors to be used in the design.

Requirements
Must have
• Use my existing card design as a starting point

```html
<!DOCTYPE html>
<html lang="en">
<head>
<meta charset="utf-8">
<title>Quillbrook Capital – Business Card</title>
<link href="https://fonts.googleapis.com/css2?family=Arimo:wght@400;700&display=swap" rel="stylesheet">
<style>
  :root {
    --backdrop: #1e1e1f;
    --card: #262627;
    --text: #ffffff;
    --muted: #d9d9d9;
    --silver: #c4c4c6;
    --foil-a: #8e8e90;
    --foil-b: #e6e6e8;
  }
  * { margin: 0; padding: 0; box-sizing: border-box; }
  html, body {
    width: 1200px; height: 895px; overflow: hidden;
    background: var(--backdrop);
    font-family: "Arimo", Helvetica, Arial, sans-serif;
    color: var(--text);
  }
  .canvas { position: relative; width: 1200px; height: 895px; }
  .card {
    position: absolute; width: 600px; height: 343px;
    background: var(--card);
    box-shadow: 0 14px 34px rgba(0,0,0,.55);
    overflow: hidden;
  }
  .card--front { left: 300px; top: 70px; }
  .card--back { left: 300px; top: 472px; }

  .brand {
    position: absolute;
    color: var(--silver);
    font-weight: 700;
    letter-spacing: .32em;
    line-height: 1.15;
    text-transform: uppercase;
  }
  .card--front .brand {
    left: 50%; top: 50%; transform: translate(-50%, -50%);
    font-size: 30px; text-align: left;
  }
  .brand__line--second { padding-left: 1.1em; }
  .card--back .brand { right: 44px; top: 40px; font-size: 21px; }

  .holder { position: absolute; left: 44px; top: 168px; }
  .holder__name { font-size: 24px; font-weight: 700; letter-spacing: .02em; }
  .holder__title { font-size: 15px; color: var(--muted); margin-top: 2px; }

  .contact { position: absolute; left: 44px; top: 232px; list-style: none; }
  .contact__item {
    display: flex; align-items: center; gap: 10px;
    font-size: 14.5px; color: var(--muted); height: 21px;
  }
  .contact__icon { width: 13px; height: 13px; fill: var(--muted); flex: none; }

  .address {
    position: absolute; right: 44px; top: 168px;
    font-size: 14.5px; line-height: 1.45; color: var(--muted); font-style: normal;
  }

  .foil {
    position: absolute; left: 0; right: 0; bottom: 0; height: 9px;
    background: linear-gradient(90deg, var(--foil-a), var(--foil-b) 40%, var(--foil-a) 70%, var(--foil-b));
  }
</style>
</head>
<body>
<main class="canvas">
  <section class="card card--front" aria-label="Card front">
    <div class="brand">
      <div class="brand__line">Quillbrook</div>
      <div class="brand__line brand__line--second">Capital</div>
    </div>
  </section>

  <section class="card card--back" aria-label="Card back">
    <div class="brand">
      <div class="brand__line">Quillbrook</div>
      <div class="brand__line brand__line--second">Capital</div>
    </div>

    <div class="holder">
      <h1 class="holder__name">MARCUS WHITFIELD</h1>
      <p class="holder__title">Finance Executive</p>
    </div>

    <ul class="contact">
      <li class="contact__item">
        <svg class="contact__icon" viewBox="0 0 16 16"><path d="M3.5 1l2.5 3-1.5 2c1 2 3 4 5 5l2-1.5 3 2.5-1.5 2.5C7 14 2 9 1 2.5z"/></svg>
        +61 7 3287 4419
      </li>
      <li class="contact__item">
        <svg class="contact__icon" viewBox="0 0 16 16"><path d="M4 0h8a1 1 0 0 1 1 1v14a1 1 0 0 1-1 1H4a1 1 0 0 1-1-1V1a1 1 0 0 1 1-1zm.5 2v10h7V2zM8 13a1 1 0 1 0 0 2 1 1 0 0 0 0-2z"/></svg>
        0471 352 608
      </li>
      <li class="contact__item">
        <svg class="contact__icon" viewBox="0 0 16 16"><path d="M1 3h14v1L8 9 1 4zm0 2.5l7 5 7-5V13H1z"/></svg>
        marcus@quillbrookcapital.com.au
      </li>
      <li class="contact__item">
        <svg class="contact__icon" viewBox="0 0 16 16"><path d="M8 1a7 7 0 1 0 0 14A7 7 0 0 0 8 1zm0 1.3c.8 0 1.8 1.7 2 4.2H6c.2-2.5 1.2-4.2 2-4.2zM2.4 7.5h2.4c0 1.1.2 2 .4 2.8H3a5.7 5.7 0 0 1-.6-2.8zm8.8 0h2.4a5.7 5.7 0 0 1-.6 2.8h-2.2c.2-.8.4-1.7.4-2.8zM6 8.8h4c-.2 2.4-1.2 4.9-2 4.9s-1.8-2.5-2-4.9z"/></svg>
        www.quillbrookcapital.com.au
      </li>
    </ul>

    <address class="address">
      Level 36 Tindale Court<br>
      58 Harwick St Brisbane<br>
      QLD 4000
    </address>

    <div class="foil"></div>
  </section>
</main>
</body>
</html>
```